Cover for Where the Quiet River Bends Beyond Our Morning

Cover for a book that describes everything that happens to a person, from pre-birth life plans through growing in compassion and wisdom to death and living in the afterlife. The information is revealed in messages from people living in the life after this life. The title is Lanterns Along the Hidden Stair of Every Soul: Gathered from Voices Dwelling in the Further Meadow. Author is T. Morven Ashdale. Book size is 6 by 9.

Target Market(s)

General

Font styles to use
Serif

```html
<!DOCTYPE html>
<html lang="en">
<head>
<meta charset="utf-8">
<title>Lanterns Along the Hidden Stair of Every Soul — Cover Presentation</title>
<link rel="stylesheet" href="https://fonts.googleapis.com/css2?family=Crimson+Pro:wght@400;500&family=EB+Garamond:wght@400&display=swap">
<style>
  :root {
    --backdrop-light: #e2e2e2;
    --backdrop-dark: #d2d2d2;
    --ink: #1b1a2a;
    --ink-soft: #2b2a36;
    --accent-red: #e01f2b;
    --cover-navy: #1f1e2b;
    --cover-white: #f3f1ee;
    --glow-copper: #b5652f;
    --glow-amber: #d8894a;
  }

  * { margin: 0; padding: 0; box-sizing: border-box; }

  html, body {
    width: 1200px;
    height: 702px;
    overflow: hidden;
  }

  body {
    position: relative;
    background: radial-gradient(ellipse at 35% 40%, var(--backdrop-light) 0%, var(--backdrop-dark) 100%);
    color: var(--ink);
    font-family: "Crimson Pro", Georgia, serif;
  }

  .design-note {
    position: absolute;
    left: 52px;
    top: 50px;
    font-family: "EB Garamond", Georgia, serif;
    font-size: 20px;
    line-height: 26.5px;
    color: var(--ink-soft);
  }

  .design-note .highlight { color: var(--accent-red); }

  .title-stack {
    position: absolute;
    left: 30px;
    top: 385px;
    width: 475px;
    text-align: center;
    color: var(--ink);
    line-height: 1;
  }

  .title-stack .lead-word {
    display: block;
    font-size: 47px;
    color: var(--accent-red);
    margin-bottom: 8px;
  }

  .title-stack .connector {
    display: block;
    font-size: 23px;
    margin-bottom: 6px;
  }

  .title-stack .main-line {
    display: block;
    font-size: 38px;
    font-weight: 500;
    margin-bottom: 8px;
  }

  .title-stack .second-line {
    display: block;
    font-size: 32px;
    font-weight: 500;
    margin-bottom: 14px;
  }

  .title-stack .subtitle {
    display: block;
    font-size: 19.5px;
  }

  .accent { color: var(--accent-red); }

  .book-cover {
    position: absolute;
    left: 735px;
    top: 60px;
    width: 390px;
    height: 585px;
    background: var(--cover-navy);
    color: var(--cover-white);
    text-align: center;
    box-shadow: 0 18px 40px rgba(0, 0, 0, 0.25);
  }

  .cover-title {
    position: absolute;
    top: 52px;
    left: 0;
    right: 0;
    line-height: 1;
  }

  .cover-title .lead-word {
    display: block;
    font-size: 34px;
    color: var(--accent-red);
    margin-bottom: 2px;
  }

  .cover-title .connector {
    display: block;
    font-size: 14px;
    margin-bottom: 5px;
  }

  .cover-title .main-line {
    display: block;
    font-size: 26px;
    margin-bottom: 4px;
  }

  .cover-title .second-line {
    display: block;
    font-size: 20px;
  }

  .cover-emblem {
    position: absolute;
    left: 35px;
    top: 185px;
    width: 320px;
    height: 320px;
  }

  .cover-subtitle {
    position: absolute;
    left: 0;
    right: 0;
    bottom: 34px;
    font-size: 16px;
    line-height: 1.35;
  }
</style>
</head>
<body>

  <p class="design-note">
    Idea behind this design<br>
    is that people who “couldn’t” be able to tell stories,<br>
    still have plenty to say and this book is a <span class="highlight">word</span> of their own.
  </p>

  <h1 class="title-stack">
    <span class="lead-word">Lanterns</span>
    <span class="connector">Along the</span>
    <span class="main-line">Hidden Stair of</span>
    <span class="second-line">Every Soul:</span>
    <span class="subtitle">Gathered from Voices Dwelling in the Further <span class="accent">Meadow.</span></span>
  </h1>

  <section class="book-cover" aria-label="Book cover">
    <div class="cover-title">
      <span class="lead-word">Lanterns</span>
      <span class="connector">along the</span>
      <span class="main-line">Hidden Stair of</span>
      <span class="second-line">Every Soul:</span>
    </div>

    <svg class="cover-emblem" viewBox="0 0 320 320" role="img"
         aria-label="Illustration: a copper coffin with a cross and a red notification badge, inside a thin ring surrounded by radiating copper rays">
      <defs>
        <radialGradient id="emblem-glow" cx="50%" cy="50%" r="50%">
          <stop offset="0%" stop-color="#d8894a" stop-opacity="0.85"/>
          <stop offset="35%" stop-color="#b5652f" stop-opacity="0.55"/>
          <stop offset="75%" stop-color="#8a4a26" stop-opacity="0.2"/>
          <stop offset="100%" stop-color="#1f1e2b" stop-opacity="0"/>
        </radialGradient>
      </defs>
      <circle cx="160" cy="160" r="160" fill="url(#emblem-glow)"/>
    </svg>

    <p class="cover-subtitle">
      Gathered from Voices Dwelling<br>
      in the Further <span class="accent">Meadow.</span>
    </p>
  </section>

</body>
</html>
```